PowerPoint Template - Korvel Mint

You find in the attached file a short description of our firm, logo, mission, vision and values. We made an empty template in order to let you free to imagine. We-have high expectations on ideas "out of the box" to merge our job (consulting firm) with Zen concept. We really Would like "Zen" look and feel, to show our difference. And we want to avoid "standard consulting" (smart guys with ties, shaking hand with Brimlo smilies ...) Thank you

Target Market(s)

organization (Rather big ones)

Industry/Entity Type

Consulting

Number of Pages Required

3 page

Font styles to use
Sans Serif

Requirements
Must have
• - Some nice pictures - Be really "Zen" (quiet, smart, luxury, people centric)
Should not have
• really looks like "standard consulting" (smart guys with ties, shaking hand with Brimlo smilies ...)

```html
<!DOCTYPE html>
<html lang="en">
<head>
<meta charset="utf-8">
<title>Korvel Mint — Presentation Template</title>
<link href="https://fonts.googleapis.com/css2?family=Carlito:wght@400;700&display=swap" rel="stylesheet">
<style>
  :root {
    --stage: #000000;
    --leaf: #9acd32;
    --leaf-soft: #cfe79a;
    --navy: #0b4a73;
    --ink: #0f466e;
    --grey: #666a6d;
    --white: #ffffff;
  }
  * { margin: 0; padding: 0; box-sizing: border-box; }
  html, body { width: 1200px; height: 1200px; overflow: hidden; background: var(--stage); }
  body { position: relative; font-family: "Carlito", "Calibri", sans-serif; color: var(--ink); }

  .slide { position: absolute; left: 81px; width: 1039px; overflow: hidden; background: var(--white); }
  .slide--cover { top: 0; height: 584px; }
  .slide--context { top: 614px; height: 585px;
    background: linear-gradient(180deg, #ffffff 6%, #eef6da 28%, #cfe69a 62%, #e6f2c8 80%, #fbfdf6 100%); }

  .top-band { position: absolute; left: 0; top: 0; width: 100%; height: 27px; background: var(--leaf); }
  .foot-band { position: absolute; left: 0; bottom: 0; width: 100%; height: 38px; background: var(--navy);
    color: var(--white); font-size: 11px; display: flex; align-items: center; }

  /* Cover */
  .brand { position: absolute; left: 0; width: 100%; top: 158px; text-align: center; }
  .brand-mark { display: block; width: 104px; height: 104px; margin: 0 auto; border: 5px solid var(--leaf); border-radius: 50%; }
  .brand-name { display: block; margin-top: 16px; color: var(--leaf); font-size: 19px; letter-spacing: 12px; padding-left: 12px; }
  .cover-title { position: absolute; left: 0; width: 100%; top: 320px; text-align: center; font-size: 68px; font-weight: 400; color: var(--ink); line-height: 1; }
  .cover-date { position: absolute; left: 0; width: 100%; top: 407px; text-align: center; font-size: 34px; color: var(--ink); line-height: 1; }
  .slide--cover .foot-band { justify-content: center; }

  /* Context */
  .context-title { position: absolute; left: 62px; top: 52px; font-size: 52px; font-weight: 400; color: var(--grey); line-height: 1; }
  .title-rule { position: absolute; left: 484px; right: 0; top: 78px; height: 2px; background: var(--leaf); }
  .facts { position: absolute; left: 62px; top: 136px; width: 860px; font-size: 20.5px; line-height: 27px; }
  .fact { display: grid; grid-template-columns: 160px 1fr; }
  .fact dt { font-weight: 700; color: var(--ink); }
  .fact dd { color: var(--ink); }
  .fact dd p + p { margin-top: 17px; }
  .fact--conv { margin-top: 14px; }
  .fact--mission { margin-top: 23px; }
  .fact--diff { margin-top: 30px; }
  .fact--conv dd { width: 630px; }
  .fact--diff dd { width: 610px; }

  .team-visual { position: absolute; right: 0; top: 250px; width: 290px; height: 297px;
    background: radial-gradient(ellipse at 70% 60%, rgba(255,255,255,0.85), rgba(220,238,180,0.5) 55%, rgba(255,255,255,0) 80%); }
  .corner-brand { position: absolute; left: 58px; bottom: 56px; color: var(--leaf); font-size: 11px; letter-spacing: 6px; display: flex; align-items: center; gap: 8px; }
  .corner-dot { width: 14px; height: 14px; border: 2px solid var(--leaf); border-radius: 50%; }
  .slide--context .foot-band { padding: 0 32px 0 57px; justify-content: space-between; }
</style>
</head>
<body>
  <section class="slide slide--cover">
    <div class="top-band"></div>
    <div class="brand">
      <span class="brand-mark"></span>
      <span class="brand-name">KORVEL MINT</span>
    </div>
    <h1 class="cover-title">Korvel Mint</h1>
    <p class="cover-date">June,2016</p>
    <footer class="foot-band">© Korvel Mint - CONFIDENTIEL</footer>
  </section>

  <section class="slide slide--context">
    <div class="top-band"></div>
    <h2 class="context-title">Activity &amp; context</h2>
    <div class="title-rule"></div>
    <dl class="facts">
      <div class="fact"><dt>Korvel Mint</dt><dd>is a management, organization and performance improvement consulting firm</dd></div>
      <div class="fact fact--conv"><dt>Our convictions:</dt><dd>in a hyper-competitive environment, only organizations able to quickly adapt will survive. Digital companies will have a competitive advantage because they will understand their ecosystem better, faster and will act more effectively than others</dd></div>
      <div class="fact fact--mission"><dt>Our mission</dt><dd>is to support the digital transformation of our clients</dd></div>
      <div class="fact fact--diff"><dt>Our differences</dt><dd><p>Use Lean and Agile known methods in innovative ways, creating quickly measurable value</p><p>Avoid stress and permanent emergency, accept mistakes to bounce back quickly</p></dd></div>
    </dl>
    <div class="team-visual" role="img" aria-label="Soft leaf shapes with white silhouettes of three standing people"></div>
    <div class="corner-brand"><span class="corner-dot"></span>KORVEL MINT</div>
    <footer class="foot-band"><span>© Korvel Mint - CONFIDENTIEL</span><span>2</span></footer>
  </section>
</body>
</html>
```